Homemaking training schools needs a Business Card design

Designer, Hello!

No special requirements, good-looking enough.
--------------------------------------------------------------------------

Name: Marcus Dale
Chairman
Tel: 0574-31759426
Mobile: 13817450926
Email: brimwell@mailtor.com
Web: www.kvd2018.com
Add: No.382, QinglanJie, BaolinQu, Ningbo, Zhejiang

LOGO
Ningbo KVD Homemaking Training School

Target Market(s)

pregnant women, mothers, infants, the elderly and families, including cleaning, cooking, nursing training.

Industry/Entity Type

Business

Contact Information for Business Card

Name: Marcus Dale
Chairman
Tel: 0574-31759426
Mobile: 13817450926
Email: brimwell@mailtor.com
Web: www.kvd2018.com

LOGO

Font styles to use
Serif
Sans Serif
Decorative

Requirements
Nice to have
• Feels: clean, specifications, safety, comfort, warmth and happiness.

```html
<!DOCTYPE html>
<html lang="en">
<head>
<meta charset="utf-8">
<title>KeVanDa Business Card</title>
<link href="https://fonts.googleapis.com/css2?family=Jost:wght@400&display=swap" rel="stylesheet">
<style>
  :root {
    --brand-blue: #0a76bd;
    --soft-blue: #8bbfe2;
    --ink: #2b2b2b;
    --card: #ffffff;
    --backdrop: #ececec;
  }
  * { margin: 0; padding: 0; box-sizing: border-box; }
  html, body { width: 1200px; height: 1194px; overflow: hidden; }
  body { background: var(--backdrop); position: relative; font-family: "Jost", sans-serif; }

  .card {
    position: absolute;
    width: 794px;
    height: 514px;
    background: var(--card);
    box-shadow: 0 4px 14px rgba(0,0,0,0.12);
    overflow: hidden;
  }
  .card--front { left: 216px; top: 56px; }
  .card--back { left: 214px; top: 622px; }

  .band { position: absolute; left: 0; width: 100%; background: var(--brand-blue); }
  .band--top { top: 0; height: 44px; }
  .band--bottom { bottom: 0; height: 42px; }

  .company-name {
    position: absolute;
    left: 0; width: 100%;
    top: 250px;
    text-align: center;
    font-family: "Jost", sans-serif;
    font-weight: 400;
    font-size: 60px;
    line-height: 1;
    color: var(--brand-blue);
  }

  .corner-shape { position: absolute; right: 0; top: 0; }

  .person { position: absolute; left: 82px; top: 78px; color: var(--brand-blue); }
  .person__name { font-size: 46px; font-weight: 400; line-height: 1; letter-spacing: 0.5px; }
  .person__role { font-size: 36px; font-weight: 400; line-height: 1; margin-top: 8px; }

  .contact-list { position: absolute; left: 84px; top: 187px; list-style: none; }
  .contact-item { position: absolute; left: 0; display: flex; align-items: center; white-space: nowrap; }
  .contact-item__icon {
    width: 54px; height: 40px;
    display: flex; align-items: center; justify-content: center;
    background: var(--brand-blue);
  }
  .contact-item__icon--soft { background: var(--soft-blue); }
  .contact-item__text { margin-left: 28px; font-size: 19px; color: var(--ink); letter-spacing: 0.6px; }
  .contact-item--mobile { top: 0; }
  .contact-item--email { top: 48px; }
  .contact-item--tel { top: 96px; }
  .contact-item--address { top: 147px; }

  .website { position: absolute; left: 84px; top: 390px; font-size: 21px; color: var(--ink); letter-spacing: 0.4px; }
</style>
</head>
<body>
  <section class="card card--front">
    <div class="band band--top"></div>
    <p class="company-name">KeVanDa</p>
    <div class="band band--bottom"></div>
  </section>

  <section class="card card--back">
    <svg class="corner-shape" width="794" height="514" viewBox="0 0 794 514" aria-hidden="true">
      <polygon points="408,0 794,0 794,486" fill="var(--brand-blue)"/>
    </svg>

    <div class="person">
      <h1 class="person__name">MARCUS DALE</h1>
      <p class="person__role">CHAIRMAN</p>
    </div>

    <ul class="contact-list">
      <li class="contact-item contact-item--mobile">
        <span class="contact-item__icon">
          <svg width="14" height="22" viewBox="0 0 14 22"><rect x="1.5" y="1.5" width="11" height="19" rx="1.5" fill="none" stroke="#fff" stroke-width="2"/><line x1="5" y1="17" x2="9" y2="17" stroke="#fff" stroke-width="1.5"/></svg>
        </span>
        <span class="contact-item__text">13817450926</span>
      </li>
      <li class="contact-item contact-item--email">
        <span class="contact-item__icon contact-item__icon--soft">
          <svg width="26" height="18" viewBox="0 0 26 18"><rect x="1" y="1" width="24" height="16" fill="none" stroke="#fff" stroke-width="1.5"/><polyline points="1,1 13,10 25,1" fill="none" stroke="#fff" stroke-width="1.5"/></svg>
        </span>
        <span class="contact-item__text">brimwell@mailtor.com</span>
      </li>
      <li class="contact-item contact-item--tel">
        <span class="contact-item__icon">
          <svg width="22" height="22" viewBox="0 0 24 24"><path fill="#fff" d="M6.6 10.8c1.4 2.8 3.8 5.1 6.6 6.6l2.2-2.2c.3-.3.7-.4 1-.2 1.1.4 2.3.6 3.6.6.6 0 1 .4 1 1V20c0 .6-.4 1-1 1C10.6 21 3 13.4 3 4c0-.6.4-1 1-1h3.5c.6 0 1 .4 1 1 0 1.3.2 2.5.6 3.6.1.3 0 .7-.2 1l-2.3 2.2z"/></svg>
        </span>
        <span class="contact-item__text">0574-31759426</span>
      </li>
      <li class="contact-item contact-item--address">
        <span class="contact-item__icon contact-item__icon--soft">
          <svg width="22" height="22" viewBox="0 0 22 22"><circle cx="11" cy="11" r="9.5" fill="none" stroke="#fff" stroke-width="1.6"/><ellipse cx="11" cy="11" rx="4" ry="9.5" fill="none" stroke="#fff" stroke-width="1.3"/><line x1="1.5" y1="11" x2="20.5" y2="11" stroke="#fff" stroke-width="1.3"/></svg>
        </span>
        <span class="contact-item__text">No.382, QinglanJie, BaolinQu, Ningbo, Zhejiang</span>
      </li>
    </ul>

    <p class="website">www.kvd2018.com</p>
  </section>
</body>
</html>
```